Law Firm Needs a new Website Design

We need a new website design for our law firm located in Manhattan (Law Offices of Tobias R. Venkland, PLLC).
We have an existing logo that we will to continue using, which can be found in www.VenklandLaw.example.
The Prime Counsel, Top Advocates Logo should also be reflected near the bottom of the Home page.
The website will be 6 pages.

Deliverables:
I want a
1) home page,
2) About Us/Practice Areas page,
3) attorneys,
4) News and Articles page, and
5) Contact and Directions/Privacy Policy page.

The colors of my logo should be in the website.
I also like a touch of black and red.

The website should project "excellence."
We seek to provide the highest quality legal services.
We handle estate planning, wills, trusts, planning for people with disabilities, asset protection and preservation, Medicaid planning, hospital safe discharge, nursing home placement, powers of attorney, health care proxies, living wills, guardianships, probate, estate administration and related litigation.

I would like the colors of my Logo used (including shading where appropriate).
I also want some black on the borders and/or bottom and some red touches throughout the page.

My Logo should appear everywhere that "Law Offices Of Tobias R. Venkland, PLLC" appears.
I want the badges for Prime counsel, Top Advocates, Top Legal Practices, and ZELQ on the Home page.
I do not want too much text on the home page.

We would also like the website to have coding.
The final design should also communicate quality, expertise and stability.
Great start so far by the people who submitted designs.
Thank you.

Industry/Entity Type

Law Firm

Coding

Coded - Design and coding required

Number of Pages Required

5+ page

Colors
3276b5
ec1f27
474747

Requirements
Must have
• Please use my logo each time you mention Law Offices of Tobias R. Venkland, PLLC. Please include the Primecounsel, Top Advocates, Top Legal Practices and Zelq rating Badges on the web home page. I only wish to be contacted by phone. I am not including testimonials and am only using the New York City address.
Nice to have
• Prefer illustrations to photos regarding practice areas
Should not have
• Testimonials, contact me by email, free consultation.

```html
<!DOCTYPE html>
<html lang="en">
<head>
<meta charset="utf-8">
<title>Law Offices of Tobias R. Venkland, PLLC</title>
<link href="https://fonts.googleapis.com/css2?family=Arimo:wght@400;700&display=swap" rel="stylesheet">
<style>
:root{
  --blue:#3276b5;
  --navy:#2b3f86;
  --form-blue:#2f5fae;
  --field-blue:#4f86d0;
  --red:#b0121b;
  --bright-red:#ec1f27;
  --ink:#222;
  --grey:#474747;
  --muted:#8a8a8a;
  --pale:#f3f3f3;
  --white:#fff;
  --dark:#1f1f1f;
}
*{margin:0;padding:0;box-sizing:border-box}
html,body{width:1200px;height:2866px;overflow:hidden;background:var(--white)}
body{font-family:"Arimo",Arial,sans-serif;color:var(--ink);position:relative}
.abs{position:absolute}
/* header */
.site-header{left:0;top:0;width:1200px;height:126px;background:var(--white)}
.brand{left:48px;top:30px;display:flex;align-items:center;gap:14px}
.brand-square{width:52px;height:52px;background:var(--navy)}
.brand-name{color:var(--navy);font-size:24px;line-height:1.15;font-weight:400}
.brand-name small{display:block;font-size:15px}
.main-nav{top:56px;font-size:14px;letter-spacing:.3px;color:var(--ink)}
.main-nav.active{color:var(--bright-red)}
/* hero */
.hero{left:0;top:126px;width:1200px;height:535px;background:linear-gradient(180deg,#c9ccd0 0%,#8d8f95 45%,#4d4a52 100%)}
.hero-caption{left:92px;top:440px;width:497px;height:133px;background:rgba(255,255,255,.82);padding:30px 0 0 18px;white-space:nowrap}
.hero-caption h1{font-weight:400;font-size:38px;line-height:44px;color:#333;letter-spacing:1px}
.hero-caption p{font-size:17px;line-height:22px;color:#333;margin-top:14px;letter-spacing:.4px}
.enquiry{left:776px;top:258px;width:332px;height:403px;background:var(--form-blue)}
.enquiry-head{height:48px;background:var(--white);color:var(--navy);font-size:22px;text-align:center;line-height:48px;font-weight:700;letter-spacing:.5px}
.field{position:absolute;left:27px;width:275px;height:40px;background:var(--field-blue);border-radius:3px;color:#fff;font-size:15px;padding:11px 14px}
.send{position:absolute;left:27px;top:332px;width:275px;height:50px;border-radius:4px;background:linear-gradient(#fff,#dcdcdc);text-align:center;line-height:50px;font-size:22px;font-weight:700;color:#222;letter-spacing:1px}
/* welcome */
.welcome-title{left:94px;top:720px;font-size:19px;color:#111;letter-spacing:.5px;font-weight:400}
.welcome-title span{color:var(--blue)}
.welcome-text{left:94px;top:758px;width:770px;font-size:12.6px;line-height:21px;color:#555}
.welcome-text p+p{margin-top:21px}
.btn-red{left:92px;top:980px;width:126px;height:36px;border-radius:18px;background:var(--red);color:#fff;font-size:14px;text-align:center;line-height:36px}
.portrait-frame{left:892px;top:720px;width:216px;height:276px;border:1px solid #ccc;padding:6px;background:#fff}
.photo{width:100%;height:100%}
/* services */
.services{left:0;top:1074px;width:1200px;height:476px;background:linear-gradient(90deg,#2a2a2a,#4a4a4a 50%,#2c2c2c)}
.section-title{width:1200px;left:0;text-align:center;font-size:30px;letter-spacing:1px;font-weight:400}
.services .section-title{color:#fff;top:54px}
.service{position:absolute;top:151px;width:250px;text-align:center;color:#fff}
.service-icon{width:118px;height:118px;border-radius:50%;background:#fff;margin:0 auto;display:flex;align-items:center;justify-content:center}
.service h3{font-weight:400;font-size:17px;margin-top:20px;letter-spacing:.5px}
.service p{font-size:13px;line-height:23px;margin-top:8px;height:46px;overflow:hidden;padding:0 18px}
.btn-ghost{width:126px;height:35px;border:1px solid #fff;border-radius:18px;margin:16px auto 0;font-size:13px;line-height:33px}
.arrow{position:absolute;width:36px;height:36px;border-radius:50%;display:flex;align-items:center;justify-content:center}
/* team */
.team .section-title{top:1616px;color:#111}
.member{position:absolute;top:1707px;width:210px}
.member-frame{height:273px;border:1px solid #ccc;padding:6px;background:#fff}
.member.featured .member-frame{border:6px solid var(--red);padding:0}
.member .exp{font-size:12.5px;color:var(--muted);margin-top:26px}
.member .name{font-size:17px;color:#333;margin-top:12px;line-height:1.15;letter-spacing:.4px}
.member.featured .name{color:var(--red)}
/* rating badges */
.ratings{left:0;top:2131px;width:1200px;height:384px;background:var(--pale)}
.badge-row{position:absolute;left:0;top:112px;width:1200px;display:flex;justify-content:center;gap:90px}
.badge{width:160px;height:160px;border-radius:50%;background:var(--white);border:8px solid var(--navy)}
.badge.alt{border-color:var(--red)}
/* footer */
.site-footer{left:0;top:2515px;width:1200px;height:275px;background:linear-gradient(180deg,var(--blue) 0%,var(--navy) 100%);color:#fff}
.footer-brand{left:96px;top:70px;width:150px;display:flex;gap:10px;align-items:center;font-size:15px;line-height:1.25}
.footer-brand .sq{width:28px;height:28px;background:#fff;flex:none}
.foot-head{font-size:18px;letter-spacing:.6px;font-weight:400}
.foot-text{font-size:13px;line-height:21px}
.news-input{left:600px;top:130px;width:277px;height:38px;background:var(--field-blue);border-radius:4px;padding:10px 14px;font-size:15px}
.subscribe{left:600px;top:179px;width:141px;height:39px;background:#fff;border-radius:4px;color:#111;font-size:15px;font-weight:700;text-align:center;line-height:39px}
.social{left:1007px;display:flex;align-items:center;gap:14px;font-size:13px}
.social i{width:34px;height:34px;border-radius:50%;border:2px solid #fff;display:block}
.copyright{left:0;top:2790px;width:1200px;height:76px;background:var(--dark);color:#ddd;font-size:13px;text-align:center;line-height:76px;letter-spacing:.3px}
</style>
</head>
<body>

<header class="abs site-header">
  <div class="abs brand">
    <div class="brand-square"></div>
    <div class="brand-name"><small>Law Offices of</small>Tobias R. Venkland<small>PLLC</small></div>
  </div>
  <a class="abs main-nav active" style="left:541px">HOME</a>
  <a class="abs main-nav" style="left:621px">TEAM</a>
  <a class="abs main-nav" style="left:697px">PRACTICE AREAS</a>
  <a class="abs main-nav" style="left:856px">PRIVACY POLICY</a>
  <a class="abs main-nav" style="left:1009px">NEWS</a>
  <a class="abs main-nav" style="left:1087px">CONTACT</a>
</header>

<section class="abs hero" role="img" aria-label="Photo of the firm's attorneys smiling around a meeting table in a bright office"></section>
<div class="abs hero-caption">
  <h1>TOBIAS R. VENKLAND</h1>
  <p>AN ELDER LAW PRACTITIONER FOR OVER 19 YEARS</p>
</div>
<form class="abs enquiry">
  <div class="enquiry-head">ENQUIRY FORM</div>
  <div class="field" style="top:80px">Your Name</div>
  <div class="field" style="top:138px">Your Phone</div>
  <div class="field" style="top:196px;height:120px">Your Message</div>
  <div class="send">SEND</div>
</form>

<h2 class="abs welcome-title">WELCOME TO <span>LAW OFFICES OF TOBIAS R. VENKLAND, PLLC</span></h2>
<div class="abs welcome-text">
  <p>Our firm was founded in 1993 by Tobias R. Venkland, a member of the National Guild of Elder Care Counsel (NGECC) and an elder law practitioner for over 19 years. Our firm is uniquely positioned to provide quality legal advice and representation in regards to estate planning, wills, trusts, planning for people with disabilities, asset protection and preservation, Medicaid planning, hospital safe discharge, nursing home placement, powers of attorney, health care proxies, living wills, guardianships, probate, estate administration and related litigation.</p>
  <p>Our familiarity with entitlement programs such as Medicaid and the statutes and regulations pertaining to them, our sensitivity to the problems and needs of seniors and our access to geriatric care managers enable us to help families preserve their life savings while planning for the care of a spouse, a parent or loved one who has dementia, Alzheimer's or other long-term health care needs.</p>
</div>
<a class="abs btn-red">Read more</a>
<div class="abs portrait-frame"><div class="photo" role="img" aria-label="Portrait of the founding attorney in a dark suit" style="background:linear-gradient(180deg,#9aa3ad,#3a3d44)"></div></div>

<section class="abs services">
  <h2 class="abs section-title">OUR SERVICE</h2>
  <div class="arrow" style="left:30px;top:192px;background:#ddd"><svg width="14" height="14" viewBox="0 0 14 14"><path d="M9 2 4 7l5 5" stroke="#333" stroke-width="2.4" fill="none"/></svg></div>
  <div class="arrow" style="left:1136px;top:192px;background:#ddd"><svg width="14" height="14" viewBox="0 0 14 14"><path d="M5 2l5 5-5 5" stroke="#333" stroke-width="2.4" fill="none"/></svg></div>

  <div class="service" style="left:74px">
    <div class="service-icon"><svg width="56" height="56" viewBox="0 0 56 56" fill="var(--form-blue)"><path d="M28 4 4 16h48z"/><rect x="6" y="18" width="44" height="4"/><rect x="10" y="24" width="5" height="20"/><rect x="19" y="24" width="5" height="20"/><rect x="28" y="24" width="5" height="20"/><rect x="37" y="24" width="5" height="20"/><rect x="6" y="46" width="44" height="5"/></svg></div>
    <h3>ESTATE PLANNING</h3>
    <p>Estate planning is not just for the very wealthy or for senior citizens</p>
    <div class="btn-ghost">Read more</div>
  </div>
  <div class="service" style="left:341px">
    <div class="service-icon"><svg width="58" height="58" viewBox="0 0 58 58" fill="var(--form-blue)"><path d="M29 8 14 21v15h30V21z"/><rect x="25" y="25" width="8" height="11" fill="#fff"/><path d="M4 30c6 0 10 8 14 14h22c4-6 8-14 14-14v6c-5 2-8 10-12 16H16C12 46 9 38 4 36z"/></svg></div>
    <h3>PROBATE AND ESTATE</h3>
    <p>Although the family is not required to retain an attorney to handle the</p>
    <div class="btn-ghost">Read more</div>
  </div>
  <div class="service" style="left:609px">
    <div class="service-icon"><svg width="56" height="56" viewBox="0 0 56 56" fill="var(--form-blue)"><g transform="rotate(45 28 28)"><rect x="16" y="8" width="24" height="10" rx="2"/><rect x="25" y="18" width="6" height="32"/></g><g transform="rotate(-45 28 28)"><rect x="16" y="8" width="24" height="10" rx="2"/><rect x="25" y="18" width="6" height="32"/></g></svg></div>
    <h3>POWERS OF ATTORNEY</h3>
    <p>Regardless of your age, it is prudent to consider what would</p>
    <div class="btn-ghost">Read more</div>
  </div>
  <div class="service" style="left:878px">
    <div class="service-icon"><svg width="60" height="56" viewBox="0 0 60 56"><path d="M30 52C8 36 2 26 2 16 2 8 9 2 17 2c6 0 10 3 13 8 3-5 7-8 13-8 8 0 15 6 15 14 0 10-6 20-28 36z" fill="var(--form-blue)"/><circle cx="30" cy="26" r="11" fill="#fff"/><path d="M30 19v14M23 26h14" stroke="var(--form-blue)" stroke-width="4"/></svg></div>
    <h3>SUPPLEMENTAL NEEDS</h3>
    <p>Eligibility for certain government benefits, such as Medicaid and</p>
    <div class="btn-ghost">Read more</div>
  </div>
</section>

<section class="team">
  <h2 class="abs section-title">OUR TEAM</h2>
  <div class="arrow" style="left:30px;top:1828px;border:1px solid #ccc;background:#fff"><svg width="14" height="14" viewBox="0 0 14 14"><path d="M9 2 4 7l5 5" stroke="#555" stroke-width="2" fill="none"/></svg></div>
  <div class="arrow" style="left:1136px;top:1828px;border:1px solid #ccc;background:#fff"><svg width="14" height="14" viewBox="0 0 14 14"><path d="M5 2l5 5-5 5" stroke="#555" stroke-width="2" fill="none"/></svg></div>

  <div class="member featured" style="left:96px">
    <div class="member-frame"><div class="photo" role="img" aria-label="Portrait of the founder and CEO" style="background:linear-gradient(180deg,#9aa3ad,#34373e)"></div></div>
    <div class="exp">Founder &amp; CEO</div>
    <div class="name">TOBIAS R. VENKLAND</div>
  </div>
  <div class="member" style="left:363px">
    <div class="member-frame"><div class="photo" role="img" aria-label="Portrait of an associate attorney in front of bookshelves" style="background:linear-gradient(180deg,#6a5a48,#8c7560 60%,#b3a79c)"></div></div>
    <div class="exp">9+ years of experience</div>
    <div class="name">MARISOL OKAFOR<br>VENKLAND</div>
  </div>
  <div class="member" style="left:629px">
    <div class="member-frame"><div class="photo" role="img" aria-label="Portrait of a senior attorney in a navy suit" style="background:linear-gradient(180deg,#a8adb4,#3a4056)"></div></div>
    <div class="exp">13+ years of experience</div>
    <div class="name">TOBIAS R. VENKLAND</div>
  </div>
  <div class="member" style="left:894px">
    <div class="member-frame"><div class="photo" role="img" aria-label="Portrait of an attorney in a dark suit and red tie" style="background:linear-gradient(180deg,#6b5640,#3a3330)"></div></div>
    <div class="exp">Founder &amp; CEO</div>
    <div class="name">HALDEN ATTORNEY</div>
  </div>
</section>

<section class="abs ratings" aria-label="Rating badges">
  <div class="badge-row">
    <div class="badge" role="img" aria-label="Prime Counsel rating badge"></div>
    <div class="badge alt" role="img" aria-label="Top Advocates rating badge"></div>
    <div class="badge" role="img" aria-label="Top Legal Practices rating badge"></div>
    <div class="badge alt" role="img" aria-label="Zelq rating badge"></div>
  </div>
</section>

<footer class="abs site-footer">
  <div class="abs footer-brand"><span class="sq"></span><span>Tobias R. Venkland</span></div>
  <h3 class="abs foot-head" style="left:290px;top:34px">MAIN OFFICE</h3>
  <p class="abs foot-text" style="left:290px;top:72px">218 Harlow Avenue, Suite 1402<br>New York, New York 10117</p>
  <p class="abs foot-text" style="left:290px;top:133px">Phone: (212) 555-0148</p>
  <p class="abs foot-text" style="left:290px;top:166px">Fax: (212) 555-0172</p>

  <h3 class="abs foot-head" style="left:600px;top:38px">NEWS LETTERS SIGN UP</h3>
  <p class="abs foot-text" style="left:600px;top:76px;line-height:19px">Sign up for our daily email by entering<br>your information below</p>
  <div class="abs news-input">Email address</div>
  <div class="abs subscribe">SUBSCRIBE</div>

  <h3 class="abs foot-head" style="left:1003px;top:38px">FOLLOW US</h3>
  <div class="abs social" style="top:71px"><i></i>Friendline</div>
  <div class="abs social" style="top:120px"><i></i>Workgrid</div>
  <div class="abs social" style="top:168px"><i></i>Chirpwave</div>
</footer>

<div class="abs copyright">© Copyright 2016 Law Offices of Tobias R. Venkland, PLLC</div>

</body>
</html>
```